Packaging Artwork for "Earth's First Expanding Biodisposable Loofah Pads"

Our company manufactures BrisaPods. They are Earth's first expanding, biodisposable loofah pads for exfoliating the skin.
BrisaPods are biodisposable, so they can be thrown-away (or composted) before nasty skin bacteria can grow on them. This makes scrubbing skin cleaner and safer.
This is a high-end product, so our packaging needs to be very clean, sophisticated and make our product look like it should be expensive. The packaging should also let the viewer know the product is environmentally friendly.
The product name is "BrisaPods". The packaging also has to say "Biodisposable".
Our new packaging is a hanging bag with a window in it. See the image attached. There is also a picture of our current packaging for our Tarnivelles sponges. We would like completely different artwork, but keep the white paper.
The attached images are of our kitchen cleaning pads "Quorlimates". This new packaging is for "BrisaPods" which are a beauty product and the artwork must be different. Also, the packaging should have a large image of the round loofah pad on the front and the image of the loofah expanding from thin to thick on the back.
Updates

This will be a 4-inch x 4-inch bag that will hang from a hook. The bag will be about 2-inches thick. The logo will be similar to the Quorlimates fish logo that has been added to the project. Instead of saying "tarnivelles", the word "BrisaPods" needs to be used in the logo.

Industry/Entity Type

health and beauty

Requirements
Must have
• slogan "Clean Germ Free. Guilt Free". The product should be called "Earth's First Expanding Biodisposable Bath Loofahs". simple clean design on a white background. see the picture of our current packaging below. We will use the same paper. We just need completely different, sophisticated artwork

```html
<!DOCTYPE html>
<html lang="en">
<head>
<meta charset="utf-8">
<title>BrisaPods – Bath Loofah Pouch Artwork</title>
<link rel="stylesheet" href="https://fonts.googleapis.com/css2?family=Montserrat:wght@200;400;500;600;800&display=swap">
<style>
  :root {
    --page: #f1f1f1;
    --pouch: #ffffff;
    --pouch-edge: #d9d9d9;
    --green: #0d5a2c;
    --ink: #2f2f2f;
    --rule: #6d6d6d;
    --logo-ink: #4b3f46;
    --logo-dot: #6aa6a4;
    --pad-light: #f6e3cf;
    --pad-mid: #ecd0b2;
    --fibre-light: #c9bda6;
    --fibre-dark: #8f856f;
    --water: #bfe3f4;
  }
  * { margin: 0; padding: 0; box-sizing: border-box; }
  html, body { width: 1200px; height: 2333px; overflow: hidden; }
  body {
    background: var(--page);
    font-family: "Montserrat", sans-serif;
    position: relative;
  }
  .pouch {
    position: absolute;
    left: 220px;
    width: 760px;
    height: 847px;
    background: var(--pouch);
    border: 14px solid #ececec;
    outline: 1px solid var(--pouch-edge);
    border-radius: 6px;
    overflow: hidden;
  }
  .pouch--front { top: 150px; }
  .pouch--window { top: 1305px; }

  .hang-slot {
    position: absolute;
    left: 306px; top: 30px;
    width: 136px; height: 24px;
    border: 2px solid var(--pouch-edge);
    border-radius: 12px;
  }
  .zip-line {
    position: absolute;
    left: 20px; right: 20px; top: 82px;
    border-top: 2px solid #e4e4e4;
  }

  .pad-window {
    position: absolute;
    left: 81px; top: 122px;
    width: 580px; height: 651px;
    border-radius: 50%;
    background: radial-gradient(ellipse at 50% 45%, var(--pad-light) 0%, var(--pad-mid) 100%);
  }

  .brand {
    position: absolute;
    left: 0; right: 0; top: 150px;
    display: flex; align-items: center; justify-content: center;
    gap: 14px;
  }
  .brand__mark {
    width: 26px; height: 26px; border-radius: 50%;
    background: var(--logo-dot);
  }
  .brand__name {
    font-weight: 400;
    font-size: 44px;
    color: var(--logo-ink);
    letter-spacing: 0.5px;
  }

  .headline {
    position: absolute;
    left: 118px; width: 525px; top: 300px;
    color: var(--green);
    text-align: center;
    line-height: 1;
  }
  .headline__kicker { font-weight: 600; font-size: 30px; letter-spacing: 0.5px; }
  .headline__expanding {
    font-weight: 200; font-size: 58px; letter-spacing: 21px;
    margin-right: -21px; margin-top: 4px;
  }
  .headline__bio { font-weight: 200; font-size: 58px; letter-spacing: 0.5px; margin-top: 2px; }
  .headline__product { font-weight: 800; font-size: 60px; margin-top: 2px; letter-spacing: 0.5px; }

  .tagline {
    margin-top: 12px;
    border-top: 1.5px solid var(--rule);
    border-bottom: 1.5px solid var(--rule);
    padding: 8px 0 7px;
    font-weight: 500; font-size: 22px;
    color: var(--ink);
    letter-spacing: 0.4px;
  }

  .expansion-illustration {
    position: absolute;
    left: 72px; top: 570px;
    width: 300px; height: 218px;
    border-radius: 46% / 40%;
    background: linear-gradient(180deg, var(--water) 0%, var(--fibre-light) 35%, var(--fibre-dark) 100%);
  }

  .features {
    position: absolute;
    left: 440px; top: 610px; width: 207px;
    list-style: none;
  }
  .features__item {
    display: flex; justify-content: flex-end; align-items: center;
    gap: 10px;
    height: 54px;
    border-bottom: 1.5px solid var(--rule);
    font-size: 19px; font-weight: 500; color: var(--ink);
  }
  .features__icon { width: 26px; height: 26px; fill: var(--green); }
</style>
</head>
<body>

  <section class="pouch pouch--front" aria-label="Pouch front, solid print">
    <div class="hang-slot"></div>
    <div class="zip-line"></div>

    <div class="brand"><span class="brand__mark"></span><span class="brand__name">BrisaPods</span></div>

    <div class="headline">
      <p class="headline__kicker">EARTH'S FIRST</p>
      <p class="headline__expanding">EXPANDING</p>
      <p class="headline__bio">BIODISPOSABLE</p>
      <p class="headline__product">BATH LOOFAHS</p>
      <p class="tagline">CLEAN GERM FREE &nbsp;|&nbsp; DISPOSE GUILT FREE</p>
    </div>

    <div class="expansion-illustration" role="img" aria-label="Illustration of a thin loofah disc splashed with water expanding into a thick pad, with mint leaves"></div>

    <ul class="features">
      <li class="features__item">All Plant
        <svg class="features__icon" viewBox="0 0 26 26"><path d="M3 5c10-2 20 1 21 2-2 9-8 14-17 12l-3 4-2-1 3-4C3 14 2 9 3 5z"/></svg></li>
      <li class="features__item">Tough
        <svg class="features__icon" viewBox="0 0 26 26"><path d="M6 22c-3-6-2-12 3-17l4 1-1 4-3 1c-1 3 0 6 2 7 3-4 8-4 11-1v5z"/></svg></li>
      <li class="features__item">Biodegradable
        <svg class="features__icon" viewBox="0 0 26 26"><path d="M13 3l4 6h-3v3h-2V9H9zM4 20l2-7 2 3 3-1 1 2-3 1 2 3zM22 20l-7 1 2-3-2-2 2-1 2 2 2-3z"/></svg></li>
    </ul>
  </section>

  <section class="pouch pouch--window" aria-label="Pouch front with round pad window">
    <div class="hang-slot"></div>
    <div class="zip-line"></div>

    <div class="pad-window" role="img" aria-label="Photograph of the round beige loofah pad with stitched edge"></div>

    <div class="brand"><span class="brand__mark"></span><span class="brand__name">BrisaPods</span></div>

    <div class="headline">
      <p class="headline__kicker">EARTH'S FIRST</p>
      <p class="headline__expanding">EXPANDING</p>
      <p class="headline__bio">BIODISPOSABLE</p>
      <p class="headline__product">BATH LOOFAHS</p>
      <p class="tagline">CLEAN GERM FREE &nbsp;|&nbsp; DISPOSE GUILT FREE</p>
    </div>

    <div class="expansion-illustration" role="img" aria-label="Illustration of a thin loofah disc splashed with water expanding into a thick pad, with mint leaves"></div>

    <ul class="features">
      <li class="features__item">All Plant
        <svg class="features__icon" viewBox="0 0 26 26"><path d="M3 5c10-2 20 1 21 2-2 9-8 14-17 12l-3 4-2-1 3-4C3 14 2 9 3 5z"/></svg></li>
      <li class="features__item">Tough
        <svg class="features__icon" viewBox="0 0 26 26"><path d="M6 22c-3-6-2-12 3-17l4 1-1 4-3 1c-1 3 0 6 2 7 3-4 8-4 11-1v5z"/></svg></li>
      <li class="features__item">Biodegradable
        <svg class="features__icon" viewBox="0 0 26 26"><path d="M13 3l4 6h-3v3h-2V9H9zM4 20l2-7 2 3 3-1 1 2-3 1 2 3zM22 20l-7 1 2-3-2-2 2-1 2 2 2-3z"/></svg></li>
    </ul>
  </section>

</body>
</html>
```